Header and Full-Page Flyer needed for 2021 Lone Range Civic Builders Summit

Save the Date Flyer and Header needed for V-OrbMQ's 2021 Lone Range Civic Builders Summit. The Lone Range Civic Builders Summit is developed by Owners, for Owners (and other industry stakeholders.

DO NOT INCLUDE This in your design - for reference on design ideas only.
About the The Lone Range Civic Builders Summit:

Are you working within the boundaries of a smaller town mentality?
Do you feel stuck within your Big City limits?

The Lone Range Civic Builders Summit is where municipalities, counties, ISD's, and other public entities will come together to share what they know, and define what they want to know more about capital project planning design, delivery, and operations.

Font styles to use
Sans Serif

Requirements
Must have
• Lone Range Civic Builders Summit
Date: August 5, 2021
Location: San Antonio, TX

```html
<!DOCTYPE html>
<html lang="en">
<head>
<meta charset="utf-8">
<title>Save the Date – Lone Range Civic Builders Summit</title>
<link rel="stylesheet" href="https://fonts.googleapis.com/css2?family=Montserrat:wght@500;600;700;800;900&display=swap">
<style>
  :root {
    --brand-blue: #1c48a5;
    --brand-green: #7cad3b;
    --ink: #222a33;
    --ink-soft: #3b434c;
    --paper: #ffffff;
    --sky-top: #f4f8fc;
    --sky-mid: #dceaf5;
  }
  * { box-sizing: border-box; margin: 0; padding: 0; }
  html, body { width: 800px; height: 1200px; overflow: hidden; background: var(--paper); }
  body { font-family: "Montserrat", Arial, sans-serif; color: var(--ink); }

  .flyer {
    position: relative;
    width: 800px;
    height: 1200px;
    overflow: hidden;
    background: linear-gradient(180deg, var(--sky-top) 0%, var(--sky-mid) 45%, #e6eff6 55%, #d6e3ec 60%);
  }

  .brand {
    position: absolute;
    top: 48px; left: 0; width: 800px;
    display: flex; justify-content: center; align-items: center; gap: 14px;
  }
  .brand-dot { width: 22px; height: 22px; border-radius: 50%; background: var(--brand-blue); }
  .brand-name {
    font-size: 30px; font-weight: 700; line-height: 1.15;
    color: var(--brand-blue);
  }

  .headline {
    position: absolute;
    top: 146px; left: 0; width: 800px;
    text-align: center; white-space: nowrap;
    font-size: 84px; font-weight: 900; letter-spacing: -1.5px;
    color: var(--brand-blue);
  }

  .about-bar {
    position: absolute;
    top: 262px; left: 57px; width: 686px; height: 44px;
    background: var(--brand-green); border-radius: 4px;
    display: flex; align-items: center; justify-content: center;
    color: var(--paper); font-size: 22px; font-weight: 600; letter-spacing: 0.4px;
    white-space: nowrap;
  }

  .intro-card {
    position: absolute;
    top: 324px; left: 57px; width: 686px;
    background: var(--paper); border-radius: 12px; overflow: hidden;
    box-shadow: 0 2px 8px rgba(30, 60, 110, 0.08);
  }
  .intro-questions {
    display: grid; grid-template-columns: 59fr 41fr;
    background: var(--brand-blue);
  }
  .intro-question {
    padding: 11px 15px;
    color: var(--paper); font-size: 12.5px; font-weight: 700; line-height: 1.35;
    text-transform: uppercase; white-space: nowrap;
  }
  .intro-question + .intro-question { border-left: 2px solid var(--paper); padding-left: 36px; }
  .intro-text {
    padding: 13px 34px 15px;
    text-align: center; font-size: 13px; font-weight: 500; line-height: 1.45;
    color: var(--ink-soft);
  }

  .event-facts {
    position: absolute;
    top: 506px; left: 57px; width: 686px;
    display: flex; align-items: center; justify-content: space-between;
  }
  .fact {
    width: 304px; height: 44px;
    display: flex; align-items: center; gap: 14px;
    border: 1.5px solid var(--brand-green); border-radius: 4px;
    background: rgba(255,255,255,0.75);
    font-size: 26px; font-weight: 800; color: var(--ink); white-space: nowrap;
  }
  .fact-icon {
    width: 42px; height: 41px; flex: none;
    display: flex; align-items: center; justify-content: center;
  }
  .fact-date .fact-icon { background: var(--brand-green); }
  .fact-place .fact-icon { background: var(--brand-blue); }
  .fact-divider { width: 2px; height: 42px; background: #8c96a0; }

  .city-photo {
    position: absolute;
    top: 570px; left: 0; width: 800px; height: 520px;
    background:
      linear-gradient(180deg, rgba(214,227,236,1) 0%, rgba(214,227,236,0) 14%),
      linear-gradient(180deg, #c9d8e2 0%, #aeb8bc 22%, #8c8f88 34%, #6e7b5c 46%, #4f6a3b 62%, #3f5a30 80%, #39532d 100%);
  }

  .footer-band {
    position: absolute;
    top: 1050px; left: 0; width: 800px; height: 150px;
  }

  .sponsor-tab {
    position: absolute;
    top: 1003px; left: 252px; width: 296px; height: 86px;
    background: var(--paper); border-radius: 26px 26px 0 0;
    display: flex; align-items: center; justify-content: center; gap: 14px;
  }
  .sponsor-dot { width: 40px; height: 40px; border-radius: 50%; background: var(--brand-blue); }
  .sponsor-name { font-size: 30px; font-weight: 700; color: var(--brand-blue); line-height: 1; }

  .contacts {
    position: absolute;
    top: 1118px; left: 40px; width: 720px;
    display: flex; align-items: stretch; justify-content: space-between;
    color: var(--paper);
  }
  .contact {
    display: flex; flex-direction: column; align-items: center; gap: 8px;
    font-size: 20px; font-weight: 600; letter-spacing: 0.3px; white-space: nowrap;
  }
  .contact-icon {
    width: 24px; height: 24px; border-radius: 50%; background: var(--paper);
    display: flex; align-items: center; justify-content: center;
  }
  .contact-divider { width: 1.5px; background: rgba(255,255,255,0.8); height: 36px; align-self: flex-end; }
</style>
</head>
<body>
<main class="flyer">

  <header class="brand">
    <span class="brand-dot"></span>
    <span class="brand-name">Lone Range Civic<br>Builders Summit</span>
  </header>

  <h1 class="headline">SAVE THE DATE</h1>

  <div class="about-bar">About the The Lone Range Civic Builders Summit</div>

  <section class="intro-card">
    <div class="intro-questions">
      <p class="intro-question">Are you working within the boundaries<br>of a smaller town mentality?</p>
      <p class="intro-question">Do you feel stuck within<br>your big city limits?</p>
    </div>
    <p class="intro-text">The Lone Range Civic Builders Summit is where municipalities, counties, ISD's, and other public entities will come together to share what they know, and define what they want to know more about capital project planning design, delivery, and operations.</p>
  </section>

  <section class="event-facts">
    <div class="fact fact-date">
      <span class="fact-icon">
        <svg width="24" height="24" viewBox="0 0 24 24" fill="none" stroke="#fff" stroke-width="1.6">
          <rect x="3" y="5" width="18" height="16" rx="2"/>
          <line x1="3" y1="10" x2="21" y2="10"/>
          <line x1="8" y1="3" x2="8" y2="7"/>
          <line x1="16" y1="3" x2="16" y2="7"/>
          <circle cx="8" cy="14" r="0.8" fill="#fff"/><circle cx="12" cy="14" r="0.8" fill="#fff"/><circle cx="16" cy="14" r="0.8" fill="#fff"/>
          <circle cx="8" cy="18" r="0.8" fill="#fff"/><circle cx="12" cy="18" r="0.8" fill="#fff"/>
        </svg>
      </span>
      <span>August 5, 2021</span>
    </div>
    <span class="fact-divider"></span>
    <div class="fact fact-place">
      <span class="fact-icon">
        <svg width="20" height="24" viewBox="0 0 20 24">
          <path d="M10 1C5 1 1.5 4.7 1.5 9.3 1.5 15 10 23 10 23s8.5-8 8.5-13.7C18.5 4.7 15 1 10 1z" fill="#fff"/>
          <circle cx="10" cy="9.3" r="3.4" fill="#1c48a5"/>
        </svg>
      </span>
      <span>San Antonio,TX</span>
    </div>
  </section>

  <div class="city-photo" role="img" aria-label="Aerial photo of a city skyline at dusk with towers rising behind a green park, river and tree-lined neighbourhoods"></div>

  <svg class="footer-band" width="800" height="150" viewBox="0 0 800 150" aria-hidden="true">
    <path d="M0 10 Q400 60 800 10 L800 150 L0 150 Z" fill="#7cad3b"/>
    <path d="M0 10 Q400 60 800 10" fill="none" stroke="#1c48a5" stroke-width="3"/>
  </svg>

  <div class="sponsor-tab">
    <span class="sponsor-dot"></span>
    <span class="sponsor-name">V-OrbMQ</span>
  </div>

  <footer class="contacts">
    <div class="contact">
      <span class="contact-icon">
        <svg width="14" height="14" viewBox="0 0 24 24"><path d="M6.6 10.8a15.1 15.1 0 0 0 6.6 6.6l2.2-2.2c.3-.3.7-.4 1-.2 1.1.4 2.3.6 3.6.6.6 0 1 .4 1 1V20c0 .6-.4 1-1 1A17 17 0 0 1 3 4c0-.6.4-1 1-1h3.5c.6 0 1 .4 1 1 0 1.3.2 2.5.6 3.6.1.3 0 .7-.2 1l-2.3 2.2z" fill="#1c48a5"/></svg>
      </span>
      <span>(555) 014-2210</span>
    </div>
    <span class="contact-divider"></span>
    <div class="contact">
      <span class="contact-icon">
        <svg width="14" height="14" viewBox="0 0 24 24"><path d="M6.6 10.8a15.1 15.1 0 0 0 6.6 6.6l2.2-2.2c.3-.3.7-.4 1-.2 1.1.4 2.3.6 3.6.6.6 0 1 .4 1 1V20c0 .6-.4 1-1 1A17 17 0 0 1 3 4c0-.6.4-1 1-1h3.5c.6 0 1 .4 1 1 0 1.3.2 2.5.6 3.6.1.3 0 .7-.2 1l-2.3 2.2z" fill="#1c48a5"/></svg>
      </span>
      <span>(555) 014-7788</span>
    </div>
    <span class="contact-divider"></span>
    <div class="contact">
      <span class="contact-icon">
        <svg width="16" height="16" viewBox="0 0 24 24" fill="none" stroke="#1c48a5" stroke-width="2">
          <circle cx="12" cy="12" r="9"/><ellipse cx="12" cy="12" rx="4" ry="9"/>
          <line x1="3" y1="12" x2="21" y2="12"/>
        </svg>
      </span>
      <span>www.v-orbmq.example.org</span>
    </div>
  </footer>

</main>
</body>
</html>
```